Summer Fun

I need a Poster for Front of hotel advertising discounted drinks on Thursday & Fridays
$3.50.
Schooners of Local Beer, Glass of House Wine & Bubbly.
From 3.30pm to 6.30 pm
Nibblies Provided

Target Market(s)

25 + Market

Industry/Entity Type

Hotel

Requirements
Should not have
• Do not want to be known as Happy Hour.

```html
<!DOCTYPE html>
<html lang="en">
<head>
<meta charset="utf-8">
<title>Discount Drinks – Thursdays and Fridays</title>
<link rel="stylesheet" href="https://fonts.googleapis.com/css2?family=Archivo+Black&family=Archivo:wght@700;800&family=Quicksand:wght@400;500&display=swap">
<style>
  :root {
    --paper: #ffffff;
    --ink: #111111;
    --shadow-grey: #bdbdbd;
    --note-yellow: #fdf08f;
    --note-edge: #f2df6b;
    --pin-green: #3c9a2c;
    --sign-red: #7a0f12;
    --sign-ring: #f1f1f1;
    --neon: #ffffff;
    --neon-glow: #ff2a2a;
    --bottle-green: #2fbf20;
    --bottle-dark: #1d7a12;
    --bottle-gold: #c7a628;
    --bottle-amber: #d98b1e;
    --outline-purple: #8a2a8c;
    --outline-teal: #1f9aa0;
  }
  * { margin: 0; padding: 0; box-sizing: border-box; }
  html, body { width: 848px; height: 1200px; overflow: hidden; background: var(--paper); }
  .poster { position: relative; width: 848px; height: 1200px; overflow: hidden; background: var(--paper); }

  .bottle-row {
    position: absolute; left: 0; top: 0; width: 848px; height: 168px;
    background: linear-gradient(180deg, var(--bottle-dark) 0%, var(--bottle-green) 55%, #9be37a 100%);
    border-bottom: 6px solid var(--bottle-gold);
  }

  .headline { position: absolute; left: 36px; top: 180px; }
  .headline__line {
    display: block; position: relative;
    font-family: "Archivo Black", "Arial Black", sans-serif;
    font-size: 136px; line-height: 112px; letter-spacing: -6px;
    color: var(--ink);
    text-shadow: 14px 12px 0 var(--shadow-grey);
  }

  .offer-note {
    position: absolute; left: 24px; top: 460px; width: 458px; height: 460px;
    background: var(--note-yellow);
    border-bottom: 4px solid var(--note-edge);
    box-shadow: 18px 14px 0 rgba(0,0,0,0.12);
    transform: rotate(-1deg);
    font-family: "Archivo", Arial, sans-serif; color: var(--ink);
  }
  .offer-note__days {
    position: absolute; left: 12px; top: 52px;
    font-weight: 800; font-size: 58px; line-height: 56px; letter-spacing: -1px;
  }
  .offer-note__items { position: absolute; left: 12px; top: 190px; list-style: none; }
  .offer-note__items li { font-weight: 700; font-size: 33px; line-height: 62px; letter-spacing: 0; }
  .offer-note__price {
    position: absolute; left: 212px; top: 340px;
    font-weight: 800; font-size: 60px; line-height: 64px; letter-spacing: -1px;
  }

  .pin { position: absolute; left: 246px; top: 434px; width: 60px; height: 60px; }

  .time-sign {
    position: absolute; left: 504px; top: 410px; width: 324px; height: 324px;
    border-radius: 50%; background: var(--sign-ring);
    box-shadow: 14px 16px 0 rgba(0,0,0,0.15);
  }
  .time-sign__face {
    position: absolute; inset: 10px; border-radius: 50%;
    background: radial-gradient(circle at 40% 35%, #a3191c 0%, var(--sign-red) 70%, #4d0608 100%);
    display: flex; flex-direction: column; align-items: center; justify-content: center;
    font-family: "Quicksand", sans-serif; color: var(--neon);
    text-shadow: 0 0 4px var(--neon-glow), 0 0 10px var(--neon-glow), 0 0 18px var(--neon-glow);
  }
  .time-sign__time { font-size: 64px; line-height: 66px; font-weight: 400; }
  .time-sign__until { font-size: 30px; line-height: 30px; font-weight: 500; color: #2a0000; text-shadow: none; }

  .wine-bottles {
    position: absolute; left: 0; top: 888px; width: 480px; height: 312px;
    background: linear-gradient(90deg, var(--bottle-gold) 0%, #9fbf3a 30%, var(--bottle-dark) 45%, #d6d02a 65%, var(--bottle-amber) 100%);
    border-top: 8px solid var(--outline-purple);
    border-right: 8px solid var(--outline-purple);
    border-radius: 40px 40px 0 0;
  }
  .beer-bottles {
    position: absolute; left: 494px; top: 752px; width: 354px; height: 448px;
    background: linear-gradient(160deg, var(--bottle-green) 0%, #57d23a 40%, var(--bottle-dark) 100%);
    border: 8px solid var(--outline-teal);
    border-right: none; border-bottom: none;
    border-radius: 60px 0 0 0;
  }
</style>
</head>
<body>
<main class="poster">
  <div class="bottle-row" role="img" aria-label="Row of green beer bottle necks along the top edge"></div>

  <h1 class="headline">
    <span class="headline__line">DISCOUNT</span>
    <span class="headline__line">DRINKS*</span>
  </h1>

  <section class="offer-note">
    <p class="offer-note__days">THURSDAYS<br>AND FRIDAYS</p>
    <ul class="offer-note__items">
      <li>Schooners of local beer</li>
      <li>Glass of house wine</li>
      <li>Bubbly</li>
    </ul>
    <p class="offer-note__price">$3.50</p>
  </section>

  <svg class="pin" viewBox="0 0 60 60" aria-hidden="true">
    <line x1="22" y1="44" x2="14" y2="56" stroke="#777" stroke-width="3"/>
    <circle cx="32" cy="28" r="20" fill="var(--pin-green)"/>
    <circle cx="26" cy="21" r="7" fill="#7fd36a"/>
  </svg>

  <div class="time-sign">
    <div class="time-sign__face">
      <span class="time-sign__time">3:30pm</span>
      <span class="time-sign__until">untill</span>
      <span class="time-sign__time">6:30pm</span>
    </div>
  </div>

  <div class="beer-bottles" role="img" aria-label="Two green beer bottles leaning in from the lower right"></div>
  <div class="wine-bottles" role="img" aria-label="Group of green, yellow and amber wine bottles in the lower left"></div>
</main>
</body>
</html>
```